Music Studio and Store Business Card and Logo Design

We need a business card and logo design for an existing Music Studio (Piano and Voice) which will soon expand to offer retail sheet music for all instruments including voice. The expanding store will not sell or lease instruments. We are a well known Fine Arts Studio for instruction to children, college students, and adults with 42 enrolled students and a wait list. We want something with simple elegance, but not archaic. Even a sleek modern look is okay. We do not want something childish or too fun looking because we do serve ages 5 - 62. We would also like the logo workable/transferable to signage for our new location opening in March. We like classic burgundy, black, deep blues, but are open to other suggestions. We included our studio brochure so you can get to know us a little better and some images we thought were interesting with the use of clef signs for the & and using note heads for the bottom or top of the letter "H"

Target Market(s)

All ages

Industry/Entity Type

Business

Contact Information for Business Card

H&H Music StudioPlattsburgh, NYWanda J. Haby and Osric M. Dunleavy, Owners

Requirements
Must have
• Phone Number: (480) 615-7094
• Website: www.rtcadenzaroom.example
Nice to have
• Email: lorna@rtcadenzaroom.example
Should not have
• Any instruments on the card other than piano. Instrument pix is not a necessity.

```html
<!DOCTYPE html>
<html lang="en">
<head>
<meta charset="utf-8">
<title>R&amp;T Music Studio — Business Card</title>
<link rel="stylesheet" href="https://fonts.googleapis.com/css2?family=Open+Sans:wght@300;400;600&display=swap">
<style>
  :root {
    --page: #e9e6e2;
    --ink: #0b0b0b;
    --paper: #fbfbfa;
    --burgundy: #8c4f5a;
    --muted: #8a8a8a;
    --text: #2a2a2a;
    --white: #ffffff;
  }
  * { margin: 0; padding: 0; box-sizing: border-box; }
  html, body { width: 1200px; height: 1062px; overflow: hidden; }
  body {
    background: var(--page);
    font-family: "Open Sans", Arial, sans-serif;
    position: relative;
  }
  .card {
    position: absolute;
    left: 320px;
    width: 560px;
    height: 320px;
    overflow: hidden;
    box-shadow: 0 10px 28px rgba(0,0,0,.25);
  }
  .card--front { top: 150px; background: var(--ink); }
  .card--back {
    top: 590px;
    background: linear-gradient(135deg, #1e1e1e 0%, #050505 60%, #111 100%);
  }
  .card__shape { position: absolute; inset: 0; }
  .brand {
    position: absolute;
    left: 0; right: 0;
    text-align: center;
    font-weight: 400;
    letter-spacing: 1px;
  }
  .card--front .brand { top: 58px; font-size: 38px; color: var(--text); }
  .card--back .brand { top: 134px; font-size: 44px; color: var(--white); }
  .details {
    position: absolute;
    left: 150px;
    top: 132px;
    color: var(--text);
  }
  .details__names { font-size: 15px; font-weight: 600; }
  .details__role { font-size: 12px; font-weight: 300; color: var(--muted); margin-bottom: 10px; }
  .contact { list-style: none; font-size: 12.5px; font-weight: 300; color: #555; }
  .contact li { display: flex; align-items: center; gap: 9px; line-height: 21px; }
  .contact svg { width: 11px; height: 11px; fill: var(--text); flex: none; }
</style>
</head>
<body>

<section class="card card--front" aria-label="Card front">
  <svg class="card__shape" viewBox="0 0 560 320" preserveAspectRatio="none">
    <ellipse cx="286" cy="160" rx="318" ry="178" fill="var(--burgundy)"/>
    <ellipse cx="280" cy="160" rx="312" ry="170" fill="var(--paper)"/>
  </svg>
  <div class="brand">R&amp;T Music Studio</div>
  <div class="details">
    <p class="details__names">Lorna K. Petrov and Osric M. Dunleavy</p>
    <p class="details__role">Owner</p>
    <ul class="contact">
      <li><svg viewBox="0 0 12 12"><path d="M2.5 0.5 L4.5 0.5 L5.2 3.2 L3.8 4.3 Q5 7 7.7 8.2 L8.8 6.8 L11.5 7.5 L11.5 9.5 Q11.5 11.5 9.5 11.5 Q1 11 0.5 2.5 Q0.5 0.5 2.5 0.5 Z"/></svg>(480) 615-7094</li>
      <li><svg viewBox="0 0 12 12"><circle cx="6" cy="6" r="5.2" fill="none" stroke="#2a2a2a" stroke-width="1.1"/><ellipse cx="6" cy="6" rx="2.2" ry="5.2" fill="none" stroke="#2a2a2a" stroke-width="1"/><path d="M1 6 H11" stroke="#2a2a2a" stroke-width="1"/></svg>www.rtcadenzaroom.example</li>
      <li><svg viewBox="0 0 12 12"><circle cx="6" cy="6" r="2.2" fill="none" stroke="#2a2a2a" stroke-width="1.3"/><path d="M8.2 6 V7.2 Q8.2 9 10 8.6 Q11.4 8 11.3 6 A5.3 5.3 0 1 0 8.6 10.6" fill="none" stroke="#2a2a2a" stroke-width="1.3"/></svg>lorna@rtcadenzaroom.example</li>
      <li><svg viewBox="0 0 12 12"><path d="M6 0.5 A4 4 0 0 1 10 4.5 Q10 7.5 6 11.5 Q2 7.5 2 4.5 A4 4 0 0 1 6 0.5 Z M6 3 A1.5 1.5 0 1 0 6 6 A1.5 1.5 0 1 0 6 3 Z" fill-rule="evenodd"/></svg>Alder Falls, NY</li>
    </ul>
  </div>
</section>

<section class="card card--back" aria-label="Card back">
  <div class="brand">R&amp;T Music Studio</div>
</section>

</body>
</html>
```